Vietnamese Restaurant Poster

We are a family restaurant specializing in Vietnamese comfort food of pho (Vietnamese Beef Noodle Soup).

We need to create a poster that will attract customers driving by our restaurant.

This poster will be placed on sandwich boards and placed on the intersecting streets.

We want it to be
- big and visually appealing.
- Preferably with a logo incorporating our name and a bowl of Pho
- a arrow sign pointing right
- our phone number 604-318-7915

The name of our restaurant is:

Pho Lanh Tuyet (Title text)
Vietnamese Restaurant (smaller text)

Reason: We have narrowed it down to 2  designs that we absolutely love. Thank you to all who have submitted.

Target Market(s)

Caucasian people who have not tried Vietnamese food. Our location is a little hidden so we want to make these posters to put on the main streets which will grab attention of people driving by to come into our restaurant

Industry/Entity Type

Restaurant

Requirements
Must have
• - big and visually appealing.
logo incorporating our name and a bowl of Pho
Nice to have
• a person eating a bowl of pho

```html
<!DOCTYPE html>
<html lang="en">
<head>
<meta charset="utf-8">
<title>Pho Lanh Tuyet – Vietnamese Restaurant</title>
<link rel="stylesheet" href="https://fonts.googleapis.com/css2?family=Cormorant+Garamond:ital,wght@1,500;1,600&family=Crimson+Text:wght@400&display=swap">
<style>
  :root {
    --maroon: #561105;
    --cream: #ffffff;
    --band-light: #8a4a3e;
    --broth: #b58860;
    --broth-mid: #c9a27a;
    --bowl: #ebe7e2;
  }
  html, body {
    margin: 0;
    padding: 0;
    overflow: hidden;
    background: var(--maroon);
  }
  .poster {
    position: relative;
    width: 1200px;
    height: 900px;
    background: var(--maroon);
    overflow: hidden;
    color: var(--cream);
  }
  .side-ornament {
    position: absolute;
    left: 72px;
    top: 0;
    width: 125px;
    height: 900px;
    background: linear-gradient(90deg, var(--maroon) 0%, var(--band-light) 50%, var(--maroon) 100%);
  }
  .title-block {
    position: absolute;
    left: 200px;
    top: 36px;
    width: 940px;
    text-align: center;
    font-family: "Cormorant Garamond", serif;
    font-style: italic;
  }
  .restaurant-name {
    margin: 0;
    font-size: 122px;
    font-weight: 600;
    line-height: 1;
    letter-spacing: 3px;
    white-space: nowrap;
  }
  .restaurant-type {
    margin: -6px 0 0 -26px;
    font-size: 64px;
    font-weight: 500;
    line-height: 1;
    letter-spacing: 2px;
    white-space: nowrap;
  }
  .dish-photo {
    position: absolute;
    left: 345px;
    top: 340px;
  }
  .direction-arrow {
    position: absolute;
    left: 840px;
    top: 318px;
  }
  .phone {
    position: absolute;
    left: 200px;
    top: 766px;
    width: 846px;
    margin: 0;
    text-align: center;
    font-family: "Crimson Text", serif;
    font-size: 62px;
    line-height: 1;
    white-space: nowrap;
  }
</style>
</head>
<body>
<main class="poster">
  <div class="side-ornament" role="img" aria-label="Decorative white wavy line running down the left edge"></div>

  <header class="title-block">
    <h1 class="restaurant-name">Pho Lanh Tuyet</h1>
    <p class="restaurant-type">Vietnamese Restaurant</p>
  </header>

  <svg class="dish-photo" width="450" height="305" viewBox="0 0 450 305" role="img" aria-label="Photo of a bowl of beef pho with rice noodles, sliced rare beef, green onion and fresh herbs in clear broth">
    <defs>
      <radialGradient id="phoTones" cx="50%" cy="42%" r="62%">
        <stop offset="0%" stop-color="var(--broth)"/>
        <stop offset="55%" stop-color="var(--broth-mid)"/>
        <stop offset="100%" stop-color="var(--bowl)"/>
      </radialGradient>
    </defs>
    <rect x="0" y="0" width="450" height="305" rx="150" ry="140" fill="url(#phoTones)"/>
  </svg>

  <svg class="direction-arrow" width="360" height="290" viewBox="0 0 360 290" role="img" aria-label="Arrow pointing right">
    <polygon points="16,82 172,82 172,14 340,142 172,272 172,198 16,198"
             fill="none" stroke="var(--cream)" stroke-width="12" stroke-linejoin="round"/>
    <polygon points="36,102 190,102 190,54 308,142 190,232 190,178 36,178"
             fill="var(--cream)"/>
  </svg>

  <p class="phone">Telephone: 604-318-7915</p>
</main>
</body>
</html>
```